Customs House descriptive business cards

We require a two-sided business card that has a simple yet elegant design. We want to be able to promote our services as a customs house. This card should include our logo, contact info and services offered with the logo being on one side and the contact info and services on the flip side

Target Market(s)

Importers / exporters to and from the Bahamas

Industry/Entity Type

Logistics

Contact Information for Business Card

The front side of the card could have the logo and the flip side should have the other relevant info

Font styles to use
Serif

Colors

Designer to choose colors to be used in the design.

Requirements
Must have
• (Harbourline Agents Ltd) Logo, address and contact info also services:
• import customs clearance, Delivery & HAndling services,Florida pickups, Export packing & Crating Services, export customs clearance, Consulting

```html
<!DOCTYPE html>
<html lang="en">
<head>
<meta charset="utf-8">
<title>Harbourline Agents Ltd — Business Card</title>
<link rel="stylesheet" href="https://fonts.googleapis.com/css2?family=Open+Sans:wght@400;600&family=Roboto:wght@500&display=swap">
<style>
  :root {
    --page-bg: #eef1f2;
    --card-white: #ffffff;
    --blue-light: #43bafb;
    --blue-deep: #2a6cf6;
    --icon-blue: #2f93f2;
    --text-dark: #1f1f1f;
    --text-white: #ffffff;
  }
  * { margin: 0; padding: 0; box-sizing: border-box; }
  html, body { width: 1200px; height: 1000px; overflow: hidden; }
  body { background: var(--page-bg); position: relative; font-family: "Open Sans", Arial, sans-serif; }

  .card { position: absolute; left: 306px; width: 605px; }
  .card--front {
    top: 106px; height: 336px;
    background: linear-gradient(180deg, var(--blue-light) 0%, var(--blue-light) 35%, var(--blue-deep) 100%);
    color: var(--text-white);
    text-align: center;
  }
  .card--back { top: 524px; height: 337px; background: var(--card-white); }

  .brand-dot {
    position: absolute; left: 50%; top: 48px; width: 70px; height: 70px;
    margin-left: -35px; border-radius: 50%; background: var(--text-white);
  }
  .brand-name {
    position: absolute; left: 0; right: 0; top: 176px;
    font-family: "Open Sans", Arial, sans-serif; font-weight: 600;
    font-size: 31px; letter-spacing: 1px; line-height: 1.2; text-transform: uppercase;
  }
  .brand-name span { display: block; font-size: 15px; letter-spacing: 6px; }
  .services {
    position: absolute; left: 0; right: 0; top: 271px;
    font-family: "Roboto", Arial, sans-serif; font-weight: 500;
    font-size: 13px; line-height: 17px; letter-spacing: 0.2px; text-transform: uppercase;
  }

  .back-brand {
    position: absolute; left: 60px; top: 120px; width: 240px; text-align: center;
    color: var(--blue-deep);
    font-weight: 600; font-size: 26px; line-height: 1.25; text-transform: uppercase;
  }
  .back-brand .brand-dot-small {
    display: block; width: 46px; height: 46px; margin: 0 auto 14px;
    border-radius: 50%; background: var(--blue-deep);
  }

  .contact-list { position: absolute; left: 342px; top: 0; list-style: none; }
  .contact-item {
    position: absolute; left: 0; width: 240px;
    display: flex; align-items: center;
    font-size: 12px; line-height: 14px; color: var(--text-dark);
  }
  .contact-icon { width: 20px; height: 20px; flex: none; margin-right: 14px; }
  .contact-icon--dot { width: 14px; height: 14px; margin: 0 17px 0 3px; border-radius: 50%; background: var(--icon-blue); }
</style>
</head>
<body>

<section class="card card--front" aria-label="Card front">
  <div class="brand-dot"></div>
  <div class="brand-name">Harbourline<span>Agents Ltd.</span></div>
  <p class="services">
    Brokerage &amp; Clearance &nbsp;• Import &amp; Export • Freight Forwarding<br>
    Packing &amp; Crating • Consulting • Doorstep Delivery
  </p>
</section>

<section class="card card--back" aria-label="Card back">
  <div class="back-brand"><span class="brand-dot-small"></span>Harbourline<br>Agents Ltd.</div>

  <ul class="contact-list">
    <li class="contact-item" style="top:68px">
      <svg class="contact-icon" viewBox="0 0 24 24"><path fill="var(--icon-blue)" d="M6.6 10.8c1.4 2.8 3.8 5.1 6.6 6.6l2.2-2.2c.3-.3.7-.4 1-.2 1.1.4 2.3.6 3.6.6.6 0 1 .4 1 1V20c0 .6-.4 1-1 1C10.6 21 3 13.4 3 4c0-.6.4-1 1-1h3.5c.6 0 1 .4 1 1 0 1.3.2 2.5.6 3.6.1.3 0 .7-.2 1z"/></svg>
      <span>Phone: 242-555-0148<br>Fax: 242-555-0148</span>
    </li>
    <li class="contact-item" style="top:110px">
      <svg class="contact-icon" viewBox="0 0 24 24"><rect x="3" y="6" width="18" height="12" rx="1" fill="var(--icon-blue)"/><path d="M3.5 6.5 12 13l8.5-6.5" stroke="#fff" stroke-width="1.4" fill="none"/></svg>
      <span>imports@harbourlineagents.com</span>
    </li>
    <li class="contact-item" style="top:149px">
      <svg class="contact-icon" viewBox="0 0 24 24" fill="none" stroke="var(--icon-blue)" stroke-width="1.6"><circle cx="12" cy="12" r="8.5"/><ellipse cx="12" cy="12" rx="3.6" ry="8.5"/><path d="M3.5 12h17M5 7.5h14M5 16.5h14"/></svg>
      <span>harbourlineagents.com</span>
    </li>
    <li class="contact-item" style="top:187px">
      <span class="contact-icon contact-icon--dot"></span>
      <span>harbourlineagents</span>
    </li>
    <li class="contact-item" style="top:225px">
      <span class="contact-icon contact-icon--dot"></span>
      <span>harbourlineagents</span>
    </li>
    <li class="contact-item" style="top:256px">
      <svg class="contact-icon" viewBox="0 0 24 24"><path fill="var(--icon-blue)" d="M12 2a7 7 0 0 0-7 7c0 5.2 7 13 7 13s7-7.8 7-13a7 7 0 0 0-7-7z"/><circle cx="12" cy="9" r="2.6" fill="#fff"/></svg>
      <span>#42 Coral Harbour Road<br>Nassau, Bahamas</span>
    </li>
  </ul>
</section>

</body>
</html>
```